Sponsor at Title Insurance Industry Seminar for Continuing Ed - 250 Companies in Attendance

I offer escrow accounting services in the Title Insurance Industry. I've attached logo files and an example of my former company. I don't like the design and it's a little wordy but it provides detail of what I offer.

Below is a brief write-up...
For professionals in the title insurance industry, finding a reliable and cost-effective solution to escrow accounting needs can feel overwhelming. When choosing the right accounting partner, title companies and law firms need a group they can trust, and that’s where we come in. Brightfen Ledger Works is a team that understands the title industry and the importance of compliance, security and accuracy. Brightfen Ledger Works is the experienced, convenient and cost-effective choice for the accounting and certification needs of companies throughout the country.

```html
<!DOCTYPE html>
<html lang="en">
<head>
<meta charset="utf-8">
<title>Brightfen Ledger Works – Flyers</title>
<link href="https://fonts.googleapis.com/css2?family=Montserrat:wght@400;500;600;700;800&display=swap" rel="stylesheet">
<style>
:root{
  --copper:#b97a63;
  --copper-dark:#a5654f;
  --navy:#2f3a4a;
  --ink:#3b3f46;
  --band:#efefef;
  --page:#e7e7e7;
  --white:#ffffff;
}
*{box-sizing:border-box;margin:0;padding:0}
html,body{width:1200px;height:3949px;overflow:hidden}
body{background:var(--page);font-family:"Montserrat",sans-serif;color:var(--ink);position:relative}
.flyer{position:absolute;left:265px;width:670px;height:867px;background:var(--white);overflow:hidden;box-shadow:0 4px 18px rgba(0,0,0,.12)}
.flyer--services{top:1090px}
.flyer--about{top:2034px}

.brand{position:absolute;left:40px;top:118px;display:flex;align-items:center;gap:10px;color:var(--copper);font-weight:700;font-size:24px;line-height:1.05;letter-spacing:.5px}
.brand__dot{width:22px;height:22px;border-radius:50%;background:var(--copper);flex:none}

.photo{position:absolute;right:0;top:0}
.photo--desk{width:431px;height:366px;background:linear-gradient(90deg,rgba(255,255,255,1) 0%,rgba(230,232,236,.6) 25%,#c9ced6 55%,#8e98a6 80%,#5d6878 100%)}
.photo--handshake{width:400px;height:375px;background:linear-gradient(90deg,rgba(255,255,255,1) 0%,#d9dde3 22%,#9aa5b4 55%,#5c6a7c 85%,#3f4a59 100%)}

.headline{position:absolute;left:40px;top:228px;font-weight:800;font-size:43px;line-height:1;text-transform:uppercase}
.headline span{display:block}
.headline .c{color:var(--copper)}
.headline .d{color:var(--navy)}
.headline--who{top:235px;font-size:55px;color:var(--copper)}

.band{position:absolute;left:0;width:100%;background:var(--band)}
.band--what{top:383px;height:130px}
.tab{position:absolute;left:46px;top:0;width:28px;height:142px;background:var(--copper);border-radius:0 0 14px 14px;display:flex;align-items:center;justify-content:center}
.tab span{transform:rotate(-90deg);white-space:nowrap;color:var(--white);font-weight:700;font-size:13px;letter-spacing:1px}
.band__text{position:absolute;left:106px;right:40px;top:18px;font-size:12.5px;line-height:1.3}
.band__text p+p{margin-top:12px;font-weight:700}

.grid{position:absolute;left:41px;top:549px;width:587px;height:225px;background:var(--copper);border-radius:16px;color:var(--white)}
.grid__line{position:absolute;background:rgba(255,255,255,.8)}
.grid__line--v{left:293px;top:0;width:2px;height:100%}
.grid__line--h{top:112px;left:0;width:100%;height:2px}
.grid__hub{position:absolute;left:254px;top:73px;width:80px;height:80px;border-radius:50%;background:var(--white)}
.cell{position:absolute;display:flex;align-items:center;gap:14px;font-size:10.5px;line-height:1.25}
.cell svg{flex:none}
.cell--tl{left:16px;top:16px;width:240px}
.cell--bl{left:16px;top:128px;width:240px}
.cell--tr{left:332px;top:14px;width:245px}
.cell--br{left:332px;top:126px;width:245px}

.footer{position:absolute;left:0;bottom:0;width:100%;height:63px;background:var(--navy);display:flex;align-items:center;padding-left:66px;color:var(--white)}
.footer__label{font-weight:800;font-size:18px;letter-spacing:.5px}
.footer__phone{margin-left:24px;height:32px;padding:0 18px 0 8px;border:2px solid var(--copper);border-radius:4px;display:flex;align-items:center;gap:10px;font-weight:700;font-size:18px;background:linear-gradient(90deg,rgba(185,122,99,.25),rgba(185,122,99,.55))}
.footer__contacts{margin-left:auto;margin-right:26px;font-size:11px;line-height:1.75}
.footer__contacts div{display:flex;align-items:center;gap:8px}
.footer__contacts i{width:11px;height:11px;border-radius:50%;border:2px solid var(--copper);display:inline-block}

.band--who{top:375px;height:103px;text-align:center;padding:16px 40px 0;font-size:13.5px;line-height:1.35}
.band--who strong{display:block;margin-top:10px;font-weight:700;font-size:14px}

.promise{position:absolute;left:40px;top:480px;width:280px;height:330px}
.promise__text{position:absolute;left:60px;top:556px;width:240px;text-align:center;font-size:12px;line-height:1.25;white-space:nowrap}
.promise__pct{position:absolute;left:60px;top:622px;width:240px;text-align:center;font-weight:800;font-size:56px;color:var(--copper);line-height:1}
.promise__list{position:absolute;left:120px;top:682px;font-weight:700;font-size:14px;line-height:1.25;color:var(--navy);list-style:none;white-space:nowrap}
.promise__list li::before{content:"";display:inline-block;width:7px;height:7px;border:1.5px solid var(--copper);border-radius:50%;margin-right:6px;vertical-align:middle}

.services__title{position:absolute;left:320px;top:502px;font-weight:800;font-size:23px;color:var(--navy)}
.service{position:absolute;left:293px;width:322px;height:46px;display:flex;align-items:center;padding-left:20px;gap:16px;color:var(--white);font-weight:600;font-size:17px;line-height:1.05}
.service svg.bg{position:absolute;left:0;top:0;z-index:0}
.service > *:not(.bg){position:relative;z-index:1}
.service--1{top:541px}
.service--2{top:601px}
.service--3{top:661px}
.services__note{position:absolute;left:320px;top:723px;width:300px;font-size:10.5px;line-height:1.3}
</style>
</head>
<body>

<section class="flyer flyer--services">
  <div class="photo photo--desk" role="img" aria-label="Photo of a professional at a desk using a calculator beside printed financial charts"></div>
  <div class="brand"><span class="brand__dot"></span><span>Brightfen<br>Ledger Works</span></div>
  <h1 class="headline"><span class="c">Escrow</span><span class="c">Accounting</span><span class="d">Services</span></h1>

  <div class="band band--what">
    <div class="tab"><span>WHAT WE DO</span></div>
    <div class="band__text">
      <p>Escrow accounting services are the core of our business. Let us deliver you peace of mind. When you partner with Brightfen Ledger Works, you know your escrow accounting is secure, accurate and compliant with industry regulations and Best Practices.</p>
      <p>Escrow Accounting Services Since every office operates differently, contact us today for an individualized rate quote for escrow account accounting services!</p>
    </div>
  </div>

  <div class="grid">
    <div class="grid__line grid__line--v"></div>
    <div class="grid__line grid__line--h"></div>
    <div class="cell cell--tl">
      <svg width="34" height="34" viewBox="0 0 34 34" fill="none" stroke="#fff" stroke-width="2.5"><path d="M8 26 L26 8"/><path d="M16 8 H26 V18"/><path d="M8 16 V26 H18"/></svg>
      <p>Daily two-way reconciling is a requirement for Best Practice Certification. Let us tailor a package to best your needs that ensures your compliance with Best Practice Standards.</p>
    </div>
    <div class="cell cell--bl">
      <svg width="40" height="32" viewBox="0 0 40 32" fill="none" stroke="#fff" stroke-width="2"><rect x="2" y="4" width="30" height="22" rx="2"/><path d="M12 12 l-4 3 4 3M22 12 l4 3 -4 3M19 10 l-4 10"/><circle cx="34" cy="25" r="5" fill="#b97a63"/></svg>
      <p>Regardless of your accounting software system, we can access your network via a secure remote connection on the days and times most convenient to you to complete your reconciliation.</p>
    </div>
    <div class="cell cell--tr">
      <svg width="30" height="30" viewBox="0 0 30 30" fill="#fff"><rect x="3" y="16" width="4" height="11"/><rect x="10" y="12" width="4" height="15"/><rect x="17" y="8" width="4" height="19"/><rect x="24" y="4" width="4" height="23"/></svg>
      <p>Comprehensive daily and monthly reports will be delivered securely to you, along with a clear breakdown of items that may need your attention. If you are required to submit reconciliations to underwriters, we can take care of that for you as well.</p>
    </div>
    <div class="cell cell--br">
      <svg width="32" height="32" viewBox="0 0 32 32" fill="none" stroke="#fff" stroke-width="2.2"><circle cx="18" cy="10" r="7"/><path d="M18 6v8M4 22 h8 l6 4 h10"/></svg>
      <p>With our low, affordable rates, your company can get a big boost in efficiency with minimal investment. Your individual rate is based on the volume of activity within your accounts. Discounts are available on multiple accounts.</p>
    </div>
    <div class="grid__hub"></div>
  </div>

  <footer class="footer">
    <span class="footer__label">CONTACT US</span>
    <span class="footer__phone"><svg width="16" height="16" viewBox="0 0 16 16"><circle cx="8" cy="8" r="8" fill="#fff"/><path d="M5 4 l2 0 1 2 -1 1 c.5 1 1.5 2 2 2 l1-1 2 1 0 2 c-4 0 -7-3 -7-7z" fill="#b97a63"/></svg>(555) 014-2270</span>
    <div class="footer__contacts">
      <div><i></i>www.BrightfenLedgerWorks.com</div>
      <div><i></i>info@brightfenledgerworks.com</div>
    </div>
  </footer>
</section>

<section class="flyer flyer--about">
  <div class="photo photo--handshake" role="img" aria-label="Photo of a smiling businessman in a checked shirt shaking hands with a client"></div>
  <div class="brand"><span class="brand__dot"></span><span>Brightfen<br>Ledger Works</span></div>
  <h1 class="headline headline--who"><span>Who</span><span>We Are</span></h1>

  <div class="band band--who">
    <p>Brightfen Ledger Works is a team of accounting experts who understand the title world and the importance of compliance, security and up-to-date books within it.</p>
    <strong>Our team of experienced professionals can be your perfect solution!</strong>
  </div>

  <svg class="promise" viewBox="0 0 280 330" fill="none"><path d="M128 6 Q140 -4 152 6 L272 153 Q280 165 272 177 L152 324 Q140 334 128 324 L8 177 Q0 165 8 153 Z" stroke="#b97a63" stroke-width="1.5" fill="#fff"/></svg>
  <p class="promise__text">Put Brightfen's<br>knowledge and<br>experience to work for you.<br>We want to help you achieve</p>
  <p class="promise__pct">100%</p>
  <ul class="promise__list"><li>COMPLIANCE</li><li>CONVENIENCE</li><li>CREDIBILITY</li></ul>

  <h2 class="services__title">OUR SERVICES</h2>
  <div class="service service--1">
    <svg class="bg" width="322" height="46" viewBox="0 0 322 46"><path d="M0 0 H300 L322 23 L300 46 H0 Z" fill="#b97a63"/></svg>
    <svg width="26" height="26" viewBox="0 0 26 26" fill="#fff"><rect x="3" y="6" width="8" height="18"/><rect x="13" y="2" width="10" height="22"/></svg>
    <span>Escrow Reconciliation<br>Services</span>
  </div>
  <div class="service service--2">
    <svg class="bg" width="322" height="46" viewBox="0 0 322 46"><path d="M0 0 H300 L322 23 L300 46 H0 Z" fill="#b97a63"/></svg>
    <svg width="26" height="26" viewBox="0 0 26 26" fill="none" stroke="#fff" stroke-width="2.2"><circle cx="13" cy="10" r="7"/><path d="M8 16 l-2 8 7-3 7 3 -2-8"/></svg>
    <span>TIBA Best Practice<br>Certification</span>
  </div>
  <div class="service service--3">
    <svg class="bg" width="322" height="46" viewBox="0 0 322 46"><path d="M0 0 H300 L322 23 L300 46 H0 Z" fill="#b97a63"/></svg>
    <svg width="26" height="26" viewBox="0 0 26 26" fill="none" stroke="#fff" stroke-width="2.2"><circle cx="14" cy="8" r="5"/><path d="M2 18 h7 l5 4 h10"/></svg>
    <span>Other Related Services</span>
  </div>
  <p class="services__note">For professionals in the title insurance industry, finding a reliable and cost-effective solution to escrow accounting needs can feel overwhelming. When choosing the right accounting partner, title companies and law firms need a group they can trust, and that's where we come in.</p>

  <footer class="footer">
    <span class="footer__label">CONTACT US</span>
    <span class="footer__phone"><svg width="16" height="16" viewBox="0 0 16 16"><circle cx="8" cy="8" r="8" fill="#fff"/><path d="M5 4 l2 0 1 2 -1 1 c.5 1 1.5 2 2 2 l1-1 2 1 0 2 c-4 0 -7-3 -7-7z" fill="#b97a63"/></svg>(555) 014-2270</span>
    <div class="footer__contacts">
      <div><i></i>www.BrightfenLedgerWorks.com</div>
      <div><i></i>info@brightfenledgerworks.com</div>
    </div>
  </footer>
</section>

</body>
</html>
```